Business Card Design

I am a Accredited RiverPath Officiant(r) (this title requires the Registered Trademark come after it). I am also A Non-Denominational Minister. My minister title is important, but not my primary focus. My primary line of business is custom weddings. I also offer other ceremonies across the range of life experiences. Right now the back of my card lists the other ceremonies I create and lead. I have a logo that was just developed and I want to use my logo for my cards. I have the logo in every possible format, color black/white also broken up with just the graphic of just the name. I can send other formats if needed. You can see info about my wedding work at www.lanternrites.com. My physical address is less important than my email and phone number. My secondary line of business is personalized funerals and memorials. The challenge is I don't want to have more than one card, but I want to separate weddings and funerals. Thinking funerals needs to go on the back. I hate my funeral website name(www.gentlepartingsne.com) but it might be important to use it.
Information on back of card currently says:
Specializing in Couples Centered Custom Wedding Ceremonies.
Addition Services: Creating ways to express the meaningful moments of your life, in your on way: Baby Welcoming's and Naming's, Mother/Father Parent Passages for birth and adoption, Engagement and Vow Renewals, New Home Dedications, Creative Business Ribbon Cuttings, Ceremonies of Transition-moving, home sale, business closing, career change, Croning. Ceremonies of Healing-divorce, job loss, recovery, rededication, Transgender Naming Ceremonies, Coming Out Ceremonies. Ceremonies to Celebrate life and honor death-custom funeral and personalized life memorials. Ceremony writing services also available.

Target Market(s)

95% of my business is wedding clients both gay and straight.Also do custom funerals.I also do other ceremony want to use only 1 card for all products

Industry/Entity Type

Wedding

Contact Information for Business Card

Marla J. Penwick, Non-Denominational Minister
Accredited River-Path Officiant(r)
Lantern Rites
217 Fenwick Rd. Alderbrook, CT 06050
8604173926
www.lanternrites.com
tag line on front Heartfelt Custom Created Ceremonies

```html
<!DOCTYPE html>
<html lang="en">
<head>
<meta charset="utf-8">
<title>Lantern Rites – Business Card</title>
<link href="https://fonts.googleapis.com/css2?family=Open+Sans:wght@400;600;700&display=swap" rel="stylesheet">
<style>
  :root {
    --page: #ecebe8;
    --paper: #ffffff;
    --teal: #0f9a88;
    --teal-mid: #0c8a79;
    --rose: #b8434a;
    --grey: #6f6f6f;
    --white: #ffffff;
  }
  * { box-sizing: border-box; margin: 0; padding: 0; }
  html, body {
    width: 1200px; height: 800px; overflow: hidden;
    background: var(--page);
    font-family: "Open Sans", Arial, sans-serif;
  }
  .canvas { position: relative; width: 1200px; height: 800px; }
  .card {
    position: absolute; top: 230px;
    width: 550px; height: 320px;
    overflow: hidden;
    box-shadow: 0 10px 28px rgba(0,0,0,.22);
  }

  /* ---------- back side ---------- */
  .card-back {
    left: 30px;
    background: linear-gradient(180deg, var(--teal) 0%, var(--teal-mid) 100%);
    color: var(--white);
  }
  .back-brand {
    position: absolute; left: 30px; right: 30px; top: 34px;
    text-align: center;
    font-size: 22px; font-weight: 600; color: var(--white);
  }
  .back-services {
    position: absolute; left: 30px; right: 30px; top: 96px;
    font-size: 12.2px; line-height: 1.55;
    text-align: justify;
  }
  .back-address {
    position: absolute; right: 30px; bottom: 14px;
    font-size: 9px; letter-spacing: .08em; text-transform: uppercase;
    opacity: .9;
  }

  /* ---------- front side ---------- */
  .card-front { left: 620px; background: var(--paper); }
  .brand {
    position: absolute; left: 30px; top: 30px;
    display: flex; align-items: center; gap: 10px;
  }
  .brand-dot {
    width: 14px; height: 14px; border-radius: 50%;
    background: var(--rose); flex: none;
  }
  .brand-name {
    font-size: 22px; font-weight: 600; color: var(--rose);
    line-height: 1.1;
  }
  .identity { position: absolute; left: 30px; top: 104px; }
  .person-name {
    font-size: 17px; font-weight: 700; color: var(--rose);
    text-transform: uppercase; letter-spacing: .02em;
  }
  .person-title { font-size: 11.5px; color: var(--grey); line-height: 1.45; }
  .person-title sup { font-size: 7px; }
  .contact-list { list-style: none; margin-top: 8px; }
  .contact-list li {
    display: flex; align-items: center; gap: 8px;
    font-size: 11.5px; color: var(--grey); line-height: 1.55;
  }
  .contact-icon {
    width: 12px; height: 12px; border-radius: 2px;
    background: var(--rose); flex: none;
    display: flex; align-items: center; justify-content: center;
  }
  .websites {
    position: absolute; left: 30px; bottom: 22px;
    font-size: 11.5px; color: var(--grey);
  }
  .tagline {
    position: absolute; right: 26px; top: 150px;
    font-size: 15px; color: var(--rose);
  }
</style>
</head>
<body>
<main class="canvas">

  <section class="card card-back" aria-label="Card back">
    <p class="back-brand">Lantern Rites</p>
    <p class="back-services">
      Creating ways to express the meaningful moments of your life, in your on way: Baby Welcoming's and Naming's, Mother/Father Parent Passages for birth and adoption, Engagement and Vow Renewals, New Home Dedications, Creative Business Ribbon Cuttings, Ceremonies of Transition-moving, home sale, business closing, career change, Croning, Ceremonies of Healing-divorce, job loss, recovery, rededication, Transgender Naming Ceremonies, Coming Out Ceremonies, Ceremonies to Celebrate life and honor death-custom funeral and personalized life memorials.
    </p>
    <p class="back-address">217 Fenwick Rd. Alderbrook, CT 06050</p>
  </section>

  <section class="card card-front" aria-label="Card front">
    <div class="brand">
      <span class="brand-dot"></span>
      <p class="brand-name">Marla Penwick Officiant</p>
    </div>

    <div class="identity">
      <h1 class="person-name">Marla J. Penwick</h1>
      <p class="person-title">Non-Denominational Minister<br>Accredited River-Path Officiant<sup>®</sup></p>
      <ul class="contact-list">
        <li><span class="contact-icon">
          <svg width="8" height="8" viewBox="0 0 24 24" aria-hidden="true"><path fill="#fff" d="M6.6 10.8a15 15 0 0 0 6.6 6.6l2.2-2.2a1 1 0 0 1 1-.25 11.4 11.4 0 0 0 3.6.57 1 1 0 0 1 1 1V20a1 1 0 0 1-1 1A17 17 0 0 1 3 4a1 1 0 0 1 1-1h3.5a1 1 0 0 1 1 1c0 1.25.2 2.45.57 3.6a1 1 0 0 1-.25 1z"/></svg>
        </span>860 417 3926</li>
        <li><span class="contact-icon"></span>/lanternrites</li>
        <li><span class="contact-icon">
          <svg width="8" height="8" viewBox="0 0 24 24" aria-hidden="true"><path fill="#fff" d="M2 5h20v14H2z M2 5l10 8 10-8" stroke="#b8434a" stroke-width="2"/></svg>
        </span>Marla@LanternRites.com</li>
        <li><span class="contact-icon">
          <svg width="8" height="8" viewBox="0 0 24 24" aria-hidden="true"><circle cx="12" cy="12" r="9" fill="none" stroke="#fff" stroke-width="3"/></svg>
        </span>www.lanternrites.com</li>
      </ul>
    </div>

    <p class="websites">www.lanternrites.com | www.gentlepartingsne.com</p>
    <p class="tagline">Because your story matters</p>
  </section>

</main>
</body>
</html>
```